Travel Business Card

Hello. I am an award-winning travel advisor in Sydney, Australia seeking new business cards reflecting a unique style. Words to describe the design I'm seeking - Contemporary, Artsy, Vibrant, Soulful, Journey.

I loved this'Absolut' design and have created a few concepts to guide you for the back of the bus card. Feel free to use your own imagination...
maybe use elements of a Venetian mask or City (Icon), Cruise Ship, Sunshine, Beach/ Beach Hut, Buddha (Spiritual), Lotus or Palm Tree (Nature), Magic Carpet (Middle East), Whale or Waves, or enhance the pencil sketch I did...

Remember. The design should look high-end and fashionable.

Looking forward to hearing from you.
My email is miriam@plenvoritrips.example.

Many thanks.

```html
<!DOCTYPE html>
<html lang="en">
<head>
<meta charset="utf-8">
<title>Miriam Carraway – Travel Advisor Business Card</title>
<link href="https://fonts.googleapis.com/css2?family=Marcellus&display=swap" rel="stylesheet">
<style>
  :root {
    --page: #ffffff;
    --card-base: #d9dcdd;
    --ring-dark: #1a1a17;
    --ring-slate: #5d6a70;
    --ring-tan: #b9ad9b;
    --core-light: #aab8bd;
    --teal: #1d8a86;
    --teal-deep: #0f6f6c;
    --brown: #4a1208;
    --white: #ffffff;
  }
  * { margin: 0; padding: 0; box-sizing: border-box; }
  html, body {
    width: 1200px; height: 1001px; overflow: hidden;
    background: var(--page);
    font-family: "Marcellus", serif;
  }
  .canvas { position: relative; width: 1200px; height: 1001px; }
  .card {
    position: absolute; border-radius: 16px; overflow: hidden;
    background: var(--card-base);
  }
  .card-front {
    left: 210px; top: 18px; width: 826px; height: 467px;
    background: radial-gradient(circle at 410px 232px,
      var(--core-light) 0, #b7b8b0 90px, var(--ring-tan) 140px,
      #7d786d 190px, var(--ring-dark) 240px, var(--ring-slate) 290px,
      #b8bec0 320px, var(--card-base) 345px);
  }
  .card-back {
    left: 208px; top: 513px; width: 833px; height: 469px;
    background: radial-gradient(circle at 432px 232px,
      #1f4a4d 0, #6d8c90 70px, #aabbc0 130px, var(--ring-tan) 185px,
      #6f6a5f 225px, var(--ring-dark) 260px, var(--ring-slate) 305px,
      #b8bec0 335px, var(--card-base) 360px);
  }
  .front-art { position: absolute; left: 0; top: 0; }
  .front-name {
    position: absolute; left: 0; right: 16px; top: 30px; text-align: center;
    color: var(--teal); font-weight: 400; font-size: 39px; line-height: 1;
  }
  .front-title {
    position: absolute; left: 0; right: 0; top: 66px; text-align: center;
    color: var(--teal); font-size: 31px; line-height: 1; padding-left: 8px;
  }
  .registration {
    position: absolute; left: 270px; top: 364px; width: 280px; text-align: center;
    color: var(--brown); font-size: 19px; line-height: 26px; letter-spacing: 0.5px;
  }
  .back-name {
    position: absolute; left: 82px; top: 174px;
    color: var(--white); font-weight: 400; font-size: 30px; line-height: 1;
  }
  .contact-list {
    position: absolute; left: 86px; top: 229px; list-style: none;
    color: var(--white); font-size: 17px; line-height: 19px; letter-spacing: 0.5px;
  }
  .divider {
    position: absolute; left: 409px; top: 163px; width: 9px; height: 156px;
    background: var(--teal-deep);
  }
  .online-list {
    position: absolute; left: 446px; top: 268px; list-style: none;
    color: var(--white); font-size: 15px; line-height: 19px;
  }
  .credentials {
    position: absolute; left: 0; right: 0; top: 334px; text-align: center;
    color: var(--white); font-size: 16px; line-height: 19px; letter-spacing: 0.5px;
  }
</style>
</head>
<body>
<main class="canvas">
  <section class="card card-front">
    <svg class="front-art" width="826" height="467" viewBox="0 0 826 467">
      <defs>
        <radialGradient id="scene-tone" cx="45%" cy="50%" r="55%">
          <stop offset="0" stop-color="#bfeee9"/>
          <stop offset="0.55" stop-color="#4fc3bb"/>
          <stop offset="0.85" stop-color="#2a9e97"/>
          <stop offset="1" stop-color="#1d8a86" stop-opacity="0.85"/>
        </radialGradient>
        <radialGradient id="bubble-tone" cx="50%" cy="50%" r="50%">
          <stop offset="0" stop-color="#8e9a9e" stop-opacity="0.75"/>
          <stop offset="0.7" stop-color="#8e9a9e" stop-opacity="0.35"/>
          <stop offset="1" stop-color="#8e9a9e" stop-opacity="0"/>
        </radialGradient>
        <radialGradient id="swirl-tone" cx="50%" cy="50%" r="50%">
          <stop offset="0" stop-color="#6a1a0c" stop-opacity="0.6"/>
          <stop offset="0.7" stop-color="#6a1a0c" stop-opacity="0.3"/>
          <stop offset="1" stop-color="#6a1a0c" stop-opacity="0"/>
        </radialGradient>
      </defs>
      <ellipse role="img" aria-label="Cluster of concentric silver bubble ornaments"
               cx="165" cy="205" rx="125" ry="110" fill="url(#bubble-tone)"/>
      <circle role="img" aria-label="Round tropical beach illustration with waves, sun, palm trees and hibiscus flowers"
              cx="402" cy="240" r="108" fill="url(#scene-tone)"/>
      <ellipse role="img" aria-label="Dark red flourish ornament with spiral"
               cx="665" cy="275" rx="100" ry="150" fill="url(#swirl-tone)"/>
    </svg>
    <h1 class="front-name">MIRIAM CARRAWAY</h1>
    <p class="front-title">TRAVEL ADVISOR</p>
    <p class="registration">LIC. NO. 2TA00000<br>ABN. 00 000 000 000</p>
  </section>

  <section class="card card-back">
    <h2 class="back-name">MIRIAM CARRAWAY</h2>
    <ul class="contact-list">
      <li>M. 0400 555 218</li>
      <li>F.&nbsp; 02 5550 7316</li>
      <li>A.&nbsp; PO BOX XXX,</li>
      <li>TALLOWEN RIDGE, NSW 2199</li>
    </ul>
    <div class="divider"></div>
    <ul class="online-list">
      <li>E. TRAVEL@MIRIAMCARRAWAY.EXAMPLE</li>
      <li>W. WWW.MIRIAMCARRAWAY.EXAMPLE</li>
    </ul>
    <p class="credentials">OVER 16 YEARS EXPERIENCE – LEISURE &amp; CORPORATE<br>AUSTRALIAN CRUISE CONSULTANT OF THE YEAR</p>
  </section>
</main>
</body>
</html>
```